A creative, unique invitation card for destination wedding

We are looking for a creative wedding invitation card for our destination wedding at Koh Samui. Wedding theme colour is in blue grey (slate blue) and khaki. We have included the one idea we have for the wedding invite (please ignore the fonts and colour). However, we would love to explore more unqiue ideas and design. Please include the photos attached and feel free to choose between the duplicates.

Target Market(s)

Friends and families

Industry/Entity Type

Wedding

Font styles to use
Sans Serif
Decorative
Script

Colors

Designer to choose colors to be used in the design.

Requirements
Must have
• Card should fit into a 110 X 220 cm envelope
Nice to have
• One design with blue grey/slate blue colour palette
Should not have
• Avoid dye cut
• Cartoons
• Primary colours

```html
<!DOCTYPE html>
<html lang="en">
<head>
<meta charset="utf-8">
<title>Wedding Invitation – Koh Samui</title>
<link rel="stylesheet" href="https://fonts.googleapis.com/css2?family=Great+Vibes&family=Montserrat:wght@500;700&display=swap">
<style>
  :root {
    --page: #ffffff;
    --slate: #9cb0bb;
    --charcoal: #3a3a3a;
    --khaki: #f0dc9a;
    --white: #ffffff;
    --sky-top: #c9d3de;
    --sky-low: #aebdcb;
    --sea: #6f9a94;
    --sand: #b59c79;
    --sand-deep: #9b8262;
  }
  * { box-sizing: border-box; margin: 0; padding: 0; }
  html, body {
    width: 1200px; height: 1200px; overflow: hidden;
    background: var(--page);
  }
  .invitation {
    position: absolute; left: 326px; top: 58px;
    width: 538px; height: 1082px;
    background: var(--slate);
    box-shadow: 0 4px 10px rgba(0,0,0,0.18);
    font-family: "Montserrat", sans-serif;
    color: var(--white);
    overflow: hidden;
  }
  .hero-photo {
    position: absolute; left: 0; top: 0; width: 538px; height: 705px;
    background: linear-gradient(to bottom,
      var(--sky-top) 0%, var(--sky-low) 51%,
      var(--sea) 52.5%, var(--sea) 58%,
      var(--sand) 63%, var(--sand-deep) 85%, var(--sand) 100%);
  }
  .frame {
    position: absolute; left: 22px; top: 26px;
    width: 495px; height: 1030px;
    border: 2px solid var(--white);
  }
  .title {
    position: absolute; left: 0; width: 100%;
    font-family: "Great Vibes", cursive;
    color: var(--white);
    text-shadow: 0 2px 3px rgba(0,0,0,0.25);
    line-height: 1;
  }
  .title-our { top: 78px; left: 168px; font-size: 78px; }
  .title-wedding { top: 142px; left: 38px; font-size: 132px; }
  .couple-names {
    position: absolute; left: 86px; top: 683px;
    width: 366px; height: 82px;
    background: var(--charcoal);
    border: 1px solid #d8dde0;
    display: flex; align-items: center; justify-content: center; gap: 24px;
    color: var(--khaki);
    font-weight: 700; font-size: 34px; letter-spacing: 2.5px;
  }
  .couple-names .amp { font-size: 22px; }
  .message {
    position: absolute; left: 0; width: 100%; text-align: center;
    font-weight: 500; font-size: 17px; letter-spacing: 1px;
  }
  .message-1 { top: 816px; }
  .message-2 { top: 848px; }
  .date {
    position: absolute; left: 0; top: 898px; width: 100%;
    display: flex; align-items: center; justify-content: center; gap: 12px;
    font-weight: 700; font-size: 30px; letter-spacing: 2px;
  }
  .date-day {
    width: 56px; height: 56px; border-radius: 50%;
    background: var(--charcoal); border: 2px solid var(--white);
    display: flex; align-items: center; justify-content: center;
    color: var(--slate); letter-spacing: 0;
  }
  .venue {
    position: absolute; left: 0; top: 958px; width: 100%; text-align: center;
    font-weight: 500; font-size: 18px; letter-spacing: 1.5px;
  }
  .rsvp {
    position: absolute; left: 174px; top: 1000px;
    width: 185px; height: 82px;
    background: var(--charcoal);
    border: 1px solid #d8dde0; border-bottom: none;
    display: flex; align-items: center; justify-content: center;
    color: var(--khaki); font-weight: 500; font-size: 16px; letter-spacing: 1px;
  }
</style>
</head>
<body>
  <main class="invitation">
    <div class="hero-photo" role="img" aria-label="Photo of the couple seen from behind, sitting together on a rock on a sandy beach facing the sea under a cloudy sky"></div>
    <div class="frame"></div>
    <h1>
      <span class="title title-our">Our</span>
      <span class="title title-wedding">Wedding</span>
    </h1>
    <div class="couple-names"><span>LOREM</span><span class="amp">&amp;</span><span>IPSUM</span></div>
    <p class="message message-1">Are getting married</p>
    <p class="message message-2">Come away with us to celebrate this union</p>
    <div class="date"><span>JUNE</span><span class="date-day">21</span><span>2018</span></div>
    <p class="venue">Koh Samui</p>
    <div class="rsvp">RSVP -555-014</div>
  </main>
</body>
</html>
```